FC Morlan - Creation of a AD banner for our yearly event

We are a local soccer club in Switzerland. We're organizing a event that will substitute to our yearly club dinner. We need a banner AD to promote on the social networks this event.
We would like to see design that use one or the 2 colors of the club (blue and red).
This Ad should link to a online shop where we can buy vouchers.

Requirements
Must have
• Logo of the club
Title : Fête des lanternes d'hiver
Call to action : Plus d'informations
Side texte : Grande Tombola
Banner size : W300xH250 or W300xH600
Nice to have
• Promotion texte: Soutenez le FC Morlan et les restaurateurs locaux

```html
<!DOCTYPE html>
<html lang="fr">
<head>
<meta charset="utf-8">
<title>FC Morlan – Fête des lanternes d'hiver</title>
<link rel="stylesheet" href="https://fonts.googleapis.com/css2?family=Roboto:wght@400;500;700&family=Roboto+Condensed:wght@700&display=swap">
<style>
  :root {
    --night: #050505;
    --gold: #d8b45a;
    --gold-bright: #f6e3a4;
    --gold-deep: #7a5a1e;
    --gold-soft: #f1d98f;
    --club-red: #e3203a;
    --white: #ffffff;
  }
  html, body {
    margin: 0;
    padding: 0;
    width: 1200px;
    height: 2400px;
    overflow: hidden;
    background: var(--night);
  }
  .banner {
    position: relative;
    width: 1200px;
    height: 2400px;
    overflow: hidden;
    background: var(--night);
    font-family: "Roboto", Arial, sans-serif;
    color: var(--white);
    text-align: center;
  }
  .banner__photo {
    position: absolute;
    left: 0;
    top: 520px;
    width: 1200px;
    height: 1220px;
    background:
      radial-gradient(ellipse 200px 160px at 600px 220px, rgba(255,246,210,0.95), rgba(246,227,164,0.55) 45%, transparent 100%),
      radial-gradient(ellipse 560px 640px at 600px 520px, rgba(216,180,90,0.9), rgba(160,120,45,0.6) 45%, rgba(90,66,22,0.3) 75%, transparent 100%),
      radial-gradient(circle 180px at 140px 900px, rgba(246,227,164,0.7), transparent 100%),
      radial-gradient(circle 180px at 1060px 880px, rgba(246,227,164,0.7), transparent 100%),
      radial-gradient(circle 120px at 980px 320px, rgba(246,227,164,0.55), transparent 100%),
      radial-gradient(circle 110px at 200px 380px, rgba(246,227,164,0.5), transparent 100%);
    -webkit-mask-image: linear-gradient(180deg, transparent 0%, #000 12%, #000 78%, transparent 100%);
    mask-image: linear-gradient(180deg, transparent 0%, #000 12%, #000 78%, transparent 100%);
  }
  .club-name {
    position: absolute;
    top: 44px;
    left: 0;
    width: 100%;
    display: flex;
    justify-content: center;
    align-items: center;
    gap: 24px;
    font-family: "Roboto Condensed", "Roboto", sans-serif;
    font-weight: 700;
    font-size: 88px;
    line-height: 1;
    letter-spacing: 1px;
    text-transform: uppercase;
    color: var(--white);
  }
  .club-name__dot {
    width: 56px;
    height: 56px;
    border-radius: 50%;
    background: var(--club-red);
  }
  .title {
    position: absolute;
    top: 1560px;
    left: 40px;
    right: 40px;
    margin: 0;
    font-weight: 700;
    font-size: 118px;
    line-height: 148px;
    letter-spacing: -1px;
    text-shadow: 0 4px 24px rgba(0,0,0,0.8);
  }
  .tagline {
    position: absolute;
    top: 1880px;
    left: 0;
    width: 100%;
    margin: 0;
    font-family: "Roboto Condensed", "Roboto", sans-serif;
    font-weight: 700;
    font-size: 62px;
    line-height: 80px;
    color: var(--gold-soft);
  }
  .cta {
    position: absolute;
    top: 2000px;
    left: 140px;
    width: 908px;
    height: 164px;
    border-radius: 82px;
    background: var(--club-red);
    color: var(--white);
    display: flex;
    align-items: center;
    justify-content: center;
    font-family: "Roboto Condensed", "Roboto", sans-serif;
    font-weight: 700;
    font-size: 76px;
    text-decoration: none;
  }
  .support {
    position: absolute;
    top: 2222px;
    left: 270px;
    right: 270px;
    margin: 0;
    font-weight: 500;
    font-size: 40px;
    line-height: 56px;
  }
</style>
</head>
<body>
  <main class="banner">
    <div class="banner__photo" role="img" aria-label="Photo de deux flûtes de champagne qui trinquent sur fond noir avec étincelles et bokeh doré"></div>

    <div class="club-name"><span class="club-name__dot"></span>FC Morlan</div>

    <h1 class="title">Fête des lanternes d'hiver</h1>
    <p class="tagline">Grande Tombola</p>
    <a class="cta" href="#">Plus d'informations</a>
    <p class="support">Soutenez le FC Morlan et les restaurateurs locaux</p>
  </main>
</body>
</html>
```